New Business Card Design Project

Use the flyer uploaded and website www.brightoakbuilders.com for inspiration.
List Our Services on Backside of business cards
Martin Hollis
Harborline Renovations Inc.
Licensed General Contractors
858-471-9063

Contact Information for Business Card

Use the flyer uploaded and website www.brightoakbuilders.com for inspiration. List Our Services on Backside of business cards Martin Hollis Harborline Renovations Inc. Licensed General Contractors 858-471-9063

```html
<!DOCTYPE html>
<html lang="en">
<head>
<meta charset="utf-8">
<title>Harborline Renovations – Business Cards</title>
<link rel="stylesheet" href="https://fonts.googleapis.com/css2?family=Cinzel:wght@400;700&family=Montserrat:wght@400;500&display=swap">
<style>
  :root {
    --backdrop: #1b1b1d;
    --card: #141416;
    --ink: #f4f4f4;
    --ink-soft: #cfcfcf;
    --shadow: rgba(0,0,0,0.6);
  }
  * { margin: 0; padding: 0; box-sizing: border-box; }
  html, body { width: 1200px; height: 912px; overflow: hidden; }
  body {
    background: var(--backdrop);
    position: relative;
    font-family: "Montserrat", sans-serif;
    color: var(--ink);
  }
  .card {
    position: absolute;
    width: 540px;
    height: 308px;
    background: var(--card);
    border-radius: 14px;
    box-shadow: 0 18px 40px var(--shadow);
  }
  .card--services { left: 50px; top: 80px; }
  .card--contact { left: 610px; top: 524px; }

  .brand-name {
    font-family: "Montserrat", sans-serif;
    font-weight: 500;
    letter-spacing: 0.18em;
    text-transform: uppercase;
    color: var(--ink);
  }

  /* Services side */
  .card--services .brand-name {
    position: absolute;
    top: 96px; left: 0; right: 0;
    text-align: center;
    font-size: 22px;
  }
  .services-list {
    position: absolute;
    top: 188px; left: 0; right: 0;
    text-align: center;
    font-size: 15px;
    line-height: 1.7;
    letter-spacing: 0.02em;
    color: var(--ink);
    list-style: none;
  }

  /* Contact side */
  .card--contact .brand-name {
    position: absolute;
    top: 36px; left: 44px;
    font-size: 17px;
  }
  .person {
    position: absolute;
    top: 96px; left: 44px;
  }
  .person-name {
    font-family: "Cinzel", serif;
    font-weight: 700;
    font-size: 22px;
    letter-spacing: 0.04em;
  }
  .person-title {
    font-size: 14px;
    letter-spacing: 0.02em;
    margin-top: 2px;
  }
  .contact-list {
    position: absolute;
    top: 170px; left: 44px;
    list-style: none;
    font-size: 14px;
    line-height: 1.75;
  }
  .contact-list li { display: flex; align-items: center; gap: 10px; }
  .contact-list svg { width: 13px; height: 13px; flex: none; }
  .company-line {
    position: absolute;
    left: 44px; bottom: 26px;
    font-size: 14px;
    color: var(--ink);
  }
</style>
</head>
<body>

  <section class="card card--services" aria-label="Business card, services side">
    <h1 class="brand-name">Harborline Renovations</h1>
    <ul class="services-list">
      <li>Painting • Flooring • Kitchens • Custom Renovations</li>
      <li>Bathrooms • Energy Efficienct Upgrades</li>
    </ul>
  </section>

  <section class="card card--contact" aria-label="Business card, contact side">
    <h2 class="brand-name">Harborline Renovations</h2>
    <div class="person">
      <p class="person-name">MARTIN HOLLIS</p>
      <p class="person-title">Licensed General Contractors</p>
    </div>
    <ul class="contact-list">
      <li>
        <svg viewBox="0 0 16 16" aria-hidden="true"><path fill="#f4f4f4" d="M3.5 1.5l2.5 0 1 3.2-1.6 1.1c.8 1.7 2.1 3 3.8 3.8l1.1-1.6 3.2 1v2.5c0 .8-.7 1.5-1.5 1.5C6.6 13 3 9.4 2 3c0-.8.7-1.5 1.5-1.5z"/></svg>
        858-471-9063
      </li>
      <li>
        <svg viewBox="0 0 16 16" aria-hidden="true"><rect x="1.5" y="3.5" width="13" height="9" fill="none" stroke="#f4f4f4" stroke-width="1.5"/><path d="M1.5 3.5l6.5 5 6.5-5" fill="none" stroke="#f4f4f4" stroke-width="1.5"/></svg>
        info@brightoakbuilders.com
      </li>
      <li>
        <svg viewBox="0 0 16 16" aria-hidden="true"><circle cx="8" cy="8" r="6.3" fill="none" stroke="#f4f4f4" stroke-width="1.4"/><path d="M1.7 8h12.6M8 1.7c-3 3.4-3 9.2 0 12.6M8 1.7c3 3.4 3 9.2 0 12.6" fill="none" stroke="#f4f4f4" stroke-width="1.1"/></svg>
        www.brightoakbuilders.com
      </li>
    </ul>
    <p class="company-line">Harborline Renovations Inc.</p>
  </section>

</body>
</html>
```